Five Quill Voices, "Drafting and Polishing Made Bright"

We need a brochure that provides background about our company, identifies our products and services and provides our contact information. If possible, We would like the designer to use an Office suite product such as Word or Publisher to create the brochure if possible. We would like photos, color, something that inspires customers to use our services. We have attached a copy of a draft brochure and we believe the text in the brochure is good, but the brochure is cold, bland and lacks color, style and a fresh quality. We would like all text in the brochure to be included as well as the attached logo and company name somewhere on the front and back of the brochure. Please feel free to resize the logo and use creative license to develop the brochure as you please. However, the brochure colors should compliment the dark blue, light blue and black colors in the logo. Most of all, the brochure needs to be engaging, inviting, fresh and ultra professional. Thanks!

Target Market(s)

Small and large scale businesses who would use self-help books, writing services for blogs and Facebook posts, newsletters and manuscript reviews.

Industry/Entity Type

Marketing

Font styles to use
Serif

Colors
0655a3
3377b5
85acd3
000000

Requirements
Must have
• -Logo and company name; text in draft brochure
• -Color and business photos which relate to the products/services provided
• -Inspiring, engaging, professional feel and style
• -I would like colors which compliment the logo colors (perhaps the colors below, but we are open to designer choices
• -Since this is a writing/editing business, something in the brochure that reflects that would be good.
Nice to have
• -Open; depends on the designer preference
• -Use of Office Word or Publisher program, but we are open to the use of other programs.
Should not have
• -Bland brochure with only text

```html
<!DOCTYPE html>
<html lang="en">
<head>
<meta charset="utf-8">
<title>Five Quill Voices – Trifold Brochure</title>
<link rel="stylesheet" href="https://fonts.googleapis.com/css2?family=Tinos:wght@400;700&display=swap">
<style>
  :root {
    --blue-deep: #0655a3;
    --blue-mid: #3377b5;
    --blue-soft: #85acd3;
    --blue-mist: #c9daee;
    --ink: #000000;
    --text: #3a3a3a;
    --paper: #ffffff;
    --frame: #9a9a9a;
    --serif: "Tinos", "Times New Roman", serif;
  }
  * { box-sizing: border-box; margin: 0; padding: 0; }
  html, body { width: 1200px; height: 956px; overflow: hidden; background: var(--paper); }
  body { font-family: var(--serif); color: var(--text); }

  .canvas { position: relative; width: 1200px; height: 956px; background: var(--paper); }

  .brochure {
    position: absolute; left: 49px; top: 27px; width: 1111px; height: 828px;
    border: 1px solid var(--frame); background: var(--paper); overflow: hidden;
  }

  .panel { position: absolute; top: 0; height: 100%; }
  .panel--inside-flap { left: 0; width: 368px; }
  .panel--back { left: 368px; width: 371px; }
  .panel--cover { left: 739px; width: 372px; }

  .fold-shade {
    position: absolute; top: 0; height: 100%; pointer-events: none;
  }
  .fold-shade--first { left: 330px; width: 90px;
    background: linear-gradient(90deg, rgba(0,0,0,0) 0%, rgba(0,0,0,0.07) 42%, rgba(0,0,0,0.02) 55%, rgba(0,0,0,0) 100%); }
  .fold-shade--second { left: 700px; width: 80px;
    background: linear-gradient(90deg, rgba(0,0,0,0) 0%, rgba(0,0,0,0.04) 48%, rgba(0,0,0,0) 100%); }

  .bloom { position: absolute; pointer-events: none; }
  .bloom--top {
    left: 328px; top: -10px; width: 556px; height: 430px;
    background: radial-gradient(ellipse 50% 58% at 50% 18%, var(--blue-deep) 0%, var(--blue-mid) 38%, var(--blue-soft) 62%, rgba(133,172,211,0.35) 82%, rgba(255,255,255,0) 100%);
  }
  .bloom--flap {
    left: -60px; top: 400px; width: 480px; height: 460px;
    background: radial-gradient(ellipse 70% 62% at 18% 70%, var(--blue-mid) 0%, var(--blue-soft) 40%, rgba(201,218,238,0.9) 62%, rgba(255,255,255,0) 100%);
  }
  .bloom--base {
    left: 330px; top: 740px; width: 300px; height: 100px;
    background: radial-gradient(ellipse 62% 90% at 25% 100%, var(--blue-deep) 0%, var(--blue-soft) 55%, rgba(255,255,255,0) 100%);
  }

  .section { position: absolute; left: 51px; width: 234px; }
  .section--newsletters { top: 68px; }
  .section--reviews { top: 255px; }
  .section__title { font-size: 15px; font-weight: 700; color: var(--blue-deep); margin-bottom: 8px; }
  .section__body { font-size: 12.6px; line-height: 17px; text-align: justify; color: var(--text); }

  .growth-chart { position: absolute; left: 70px; top: 480px; width: 214px; height: 140px; }

  .consult-call {
    position: absolute; left: 30px; top: 632px; width: 310px;
    font-size: 13px; font-weight: 700; line-height: 17px; text-align: center; color: var(--ink);
  }

  .back-title { position: absolute; left: 0; width: 100%; top: 566px; text-align: center; }
  .back-title__name { font-size: 19px; letter-spacing: 1px; color: var(--blue-deep); text-transform: uppercase; }
  .back-title__tagline { font-size: 11.5px; color: var(--ink); margin-top: 4px; }

  .wordmark { position: absolute; display: flex; align-items: center; gap: 12px; }
  .wordmark__square { width: 34px; height: 34px; background: var(--blue-deep); flex: none; }
  .wordmark__name { font-family: var(--serif); font-size: 23px; font-weight: 700; color: var(--ink); white-space: nowrap; }
  .wordmark--back { left: 82px; top: 655px; }
  .wordmark--cover { left: 100px; top: 364px; }

  .contact { position: absolute; left: 76px; top: 512px; width: 270px; }
  .contact__address { font-size: 19px; line-height: 33px; letter-spacing: 0.6px; color: var(--blue-deep); text-transform: uppercase; }
  .contact__phone { font-size: 15px; color: var(--blue-deep); margin-top: 4px; }
  .contact__rule { width: 206px; height: 1px; background: var(--ink); margin-top: 80px; }
  .contact__email { font-size: 12px; color: var(--ink); margin-top: 12px; }
</style>
</head>
<body>
<div class="canvas">
  <div class="brochure">

    <div class="bloom bloom--flap" role="img" aria-label="Soft blue flower petals sweeping across the lower flap"></div>
    <div class="bloom bloom--top" role="img" aria-label="Large blue layered flower petals spreading from the top fold"></div>
    <div class="bloom bloom--base" role="img" aria-label="Blue petal edge rising from the bottom of the back panel"></div>

    <section class="panel panel--inside-flap">
      <div class="section section--newsletters">
        <h2 class="section__title">Newsletters</h2>
        <p class="section__body">Email newsletters allow you to keep current and prospective customers informed about your brand and engaged with your product and service offerings. Newsletters represent an ideal path to identify target audiences and maintain open lines of communication to encourage prospective sales/services.</p>
      </div>
      <div class="section section--reviews">
        <h2 class="section__title">Manuscript reviews</h2>
        <p class="section__body">As published writers, we understand the value of reviews and we see reviews as a collaborative process that allows manuscripts to be evaluated and commented upon by experts within the same field of research. The evaluation and critique generated from the review provides authors with feedback to improve their work and allows editors to assess the manuscript suitability for publication.</p>
      </div>

      <svg class="growth-chart" viewBox="0 0 214 140" aria-label="Line chart showing rising results">
        <g stroke="#9fb4c8" stroke-width="1">
          <line x1="24" y1="0" x2="24" y2="130"/><line x1="48" y1="0" x2="48" y2="130"/>
          <line x1="72" y1="0" x2="72" y2="130"/><line x1="96" y1="0" x2="96" y2="130"/>
          <line x1="120" y1="0" x2="120" y2="130"/><line x1="144" y1="0" x2="144" y2="130"/>
          <line x1="168" y1="0" x2="168" y2="130"/><line x1="192" y1="0" x2="192" y2="130"/>
          <line x1="0" y1="22" x2="214" y2="22"/><line x1="0" y1="48" x2="214" y2="48"/>
          <line x1="0" y1="74" x2="214" y2="74"/><line x1="0" y1="100" x2="214" y2="100"/>
        </g>
        <g stroke="#333" stroke-width="1.4">
          <line x1="1" y1="0" x2="1" y2="131"/><line x1="0" y1="130" x2="214" y2="130"/>
        </g>
        <polyline fill="none" stroke="var(--blue-mid)" stroke-width="2.2" points="1,82 18,112 40,70 76,96 112,14 150,106 212,56"/>
      </svg>

      <p class="consult-call">Contact us for a free consultation with one of our seasoned staff of writers and/or editors to help guide you along the path to success!</p>
    </section>

    <section class="panel panel--back">
      <div class="back-title">
        <p class="back-title__name">Five Quill Voices</p>
        <p class="back-title__tagline">"Drafting and Polishing Made Bright"</p>
      </div>
      <div class="wordmark wordmark--back">
        <span class="wordmark__square"></span>
        <span class="wordmark__name">Five Quill Voices</span>
      </div>
    </section>

    <section class="panel panel--cover">
      <div class="wordmark wordmark--cover">
        <span class="wordmark__square"></span>
        <span class="wordmark__name">Five Quill Voices</span>
      </div>
      <div class="contact">
        <p class="contact__address">4870 Lantern Row,<br>#20417</p>
        <p class="contact__phone">555/014-3920</p>
        <div class="contact__rule"></div>
        <p class="contact__email">fivequillvoices@mail.example</p>
      </div>
    </section>

    <div class="fold-shade fold-shade--first"></div>
    <div class="fold-shade fold-shade--second"></div>
  </div>
</div>
</body>
</html>
```